Small boutique Accounting firm needs a tax promotion flyer that stands out

We are an Accounting, taxation and Mortgage Broking firm and looking to promote our services during tax season.
We want to give a new design for our existing flyer on one side. You may consider changing the layout and design, preferably with same content.
Other side, we need a new design to simply communicate that we are Accountants, Tax Agents and Mortgage Brokers too. These three words can be scattered on the page or whatever the way you prefer. You may use our logo and tagline as a background or watermark etc. Feel free to try other colors. At the bottom of this one, we need a disclaimer similar to what we have on our existing flyer.
We may consider using each of these pages on our pinwheelo as a header image or on our website.

Target Market(s)

Individuals and Small businesses

Industry/Entity Type

Accounting

Requirements
Must have
• Please note this is DL size flyer.

```html
<!DOCTYPE html>
<html lang="en">
<head>
<meta charset="utf-8">
<title>Tallyra – Personal Tax Returns Flyer</title>
<link href="https://fonts.googleapis.com/css2?family=Josefin+Sans:wght@300;400;600;700&family=Open+Sans:wght@400;600;700;800&display=swap" rel="stylesheet">
<style>
:root{
  --bg:#8a8a8a;
  --green:#7ac143;
  --ink:#2b2b2b;
  --grey:#5a5a5a;
  --white:#ffffff;
  --paper:#f4f4f4;
  --muted:#d8d8d8;
}
*{margin:0;padding:0;box-sizing:border-box}
html,body{width:1200px;height:1000px;overflow:hidden;background:var(--bg)}
.flyer{
  position:absolute;left:269px;top:31px;width:466px;height:660px;
  transform:scale(1.42);transform-origin:0 0;
  background:var(--paper);overflow:hidden;
  font-family:"Josefin Sans",sans-serif;color:var(--white);
  box-shadow:0 4px 14px rgba(0,0,0,.25);
}
.abs{position:absolute}
.hero-photo{left:0;top:0;width:466px;height:405px;
  background:linear-gradient(180deg,#9a9a9a 0%,#6d6d6d 35%,#7c7c7c 62%,#3a3a3a 84%,#111 100%),#777;
}
.hero-photo::after{content:"";position:absolute;inset:0;
  background:radial-gradient(ellipse at 78% 40%,rgba(20,20,20,.55),transparent 55%);}
.band{left:0;top:404px;width:466px;height:16px;background:var(--green)}
.plan-area{left:0;top:420px;width:466px;height:240px;
  background:linear-gradient(180deg,#ffffff 0%,#f0f0f0 60%,#e6e6e6 100%)}
.title{left:12px;top:30px;line-height:1;text-shadow:0 1px 2px rgba(0,0,0,.35)}
.title .big{font-weight:700;font-size:38px;letter-spacing:.5px;display:block}
.title .sub{font-weight:400;font-size:27px;display:block;margin-top:4px}
.badge{width:106px;height:106px;border-radius:50%;background:var(--green);
  color:var(--white);text-align:center;display:flex;flex-direction:column;
  align-items:center;justify-content:center;border:2px solid rgba(255,255,255,.6)}
.badge .label{font-size:12px;letter-spacing:.5px}
.badge .price{font-family:"Open Sans",sans-serif;font-weight:800;font-size:38px;line-height:1}
.badge .price sup{font-size:16px;vertical-align:top;position:relative;top:4px}
.badge .note{font-size:8px;font-weight:600;line-height:1.1}
.badge .fine{font-size:5.5px;font-weight:700;line-height:1.2;font-family:"Open Sans",sans-serif}
.badge-only{left:221px;top:7px}
.badge-save{left:345px;top:7px}
.services{left:14px;top:120px}
.services h2{font-weight:700;font-size:15px;margin-bottom:9px}
.services li{list-style:none;font-weight:600;font-size:10.2px;line-height:20.5px;letter-spacing:.2px}
.office h3{font-weight:700;font-size:14px;letter-spacing:.3px;margin-bottom:4px}
.office p{font-size:10.5px;font-weight:300;line-height:1.4;color:#f0f0f0}
.office-linford{left:15px;top:230px}
.office-carrow{left:254px;top:225px}
.office-brenton{left:15px;top:298px}
.contact-box{left:250px;top:290px;width:166px;height:38px;
  border:1px solid rgba(255,255,255,.45);padding:3px 4px;font-size:10.5px;font-weight:300;line-height:1.5}
.brand-seal{left:173px;top:340px;width:120px;height:120px;border-radius:50%;
  background:var(--white);display:flex;align-items:center;justify-content:center;
  box-shadow:0 2px 6px rgba(0,0,0,.25)}
.brand-seal span{font-weight:700;font-size:22px;color:var(--ink)}
.dark{color:var(--ink)}
.group h4{font-weight:400;font-size:14.5px;color:var(--green);line-height:1}
.group .lead{font-size:7.2px;font-weight:600;color:var(--ink);margin:3px 0 5px;font-family:"Open Sans",sans-serif}
.group li{list-style:none;font-size:5.8px;font-family:"Open Sans",sans-serif;color:var(--ink);line-height:12.2px;font-weight:600}
.group-investors{left:8px;top:437px}
.group-buyers{left:68px;top:513px}
.consult{left:262px;top:482px;width:192px;height:144px;
  border:1.3px dashed #555;padding:12px 10px;color:var(--ink);
  background:rgba(255,255,255,.7)}
.consult .line1{font-size:12px;font-weight:400}
.consult .line1 b{color:var(--green);font-weight:700;font-size:18px}
.consult .line2{font-size:10px;font-weight:400;margin-top:1px}
.consult .line3{font-family:"Open Sans",sans-serif;font-weight:700;font-size:14.5px;margin:6px 0 10px}
.consult p{font-size:9px;font-weight:300;line-height:1.7}
.disclaimer{left:0;top:645px;width:466px;text-align:center;font-family:"Open Sans",sans-serif;
  font-size:6px;color:var(--grey)}
</style>
</head>
<body>
<main class="flyer">
  <div class="abs hero-photo" role="img" aria-label="Photo of a person in a suit signing documents at a desk"></div>
  <div class="abs plan-area" role="img" aria-label="Faint architectural floor plan drawing"></div>
  <div class="abs band"></div>

  <h1 class="abs title"><span class="big">PERSONAL</span><span class="sub">TAX RETURNS</span></h1>

  <div class="abs badge badge-only">
    <span class="label">ONLY</span>
    <span class="price"><sup>$</sup>90</span>
    <span class="note">PER RETURN</span>
  </div>
  <div class="abs badge badge-save">
    <span class="label">SAVE</span>
    <span class="price"><sup>$</sup>10</span>
    <span class="fine">WITH 2 OR MORE RETURNS<br>AT ONE TIME<br>$80 PER RETURN</span>
  </div>

  <section class="abs services">
    <h2>WE SPECIALIZE IN:</h2>
    <ul>
      <li>RENTAL/BUSINESS/INVESTMENT INCOME RETURNS FROM $130</li>
      <li>FINANCIAL STATEMENTS FOR BUSINESSES &amp; SMSF'S</li>
      <li>BOOK-KEEPING, BASRETURNS &amp; PAY-ROLL FROM $35 PER HOUR</li>
      <li>FORMATION OF TRUSTS, COMPANIES &amp; SMSFS</li>
    </ul>
  </section>

  <div class="abs office office-linford">
    <h3>LINFORD OFFICE</h3>
    <p>4/212 MARLOW RD LINFORD QLD 4190<br>[PLAZA COMPLEX]<br>07 3100 2481</p>
  </div>
  <div class="abs office office-carrow">
    <h3>CARROW OFFICE</h3>
    <p>7/44 ASHBY ST CARROW QLD 4355<br>07 3100 5937</p>
  </div>
  <div class="abs office office-brenton">
    <h3>BRENTON OFFICE</h3>
    <p>15 WATTLE CCT BRENTON<br>QLD 4175<br>07 3100 6624</p>
  </div>
  <div class="abs contact-box">E: ADMIN@TALLYRA.NET.AU<br>F: 07 3100 7150</div>

  <div class="abs brand-seal"><span>tallyra</span></div>

  <section class="abs group group-investors">
    <h4>INVESTORS</h4>
    <p class="lead">WE PROVIDE ASSISTANCE WITH:</p>
    <ul><li>NEGATIVE GEARING</li><li>TAX PLANNING</li><li>RE-FINANCING</li><li>SMSF LOANS</li><li>NRAS LOANS</li></ul>
  </section>
  <section class="abs group group-buyers">
    <h4>FIRST TIME HOME BUYERS</h4>
    <p class="lead">WE CAN HELP YOU UNDERSTAND:</p>
    <ul><li>5% GENUINE SAVINGS</li><li>FIXED/VARIABLE LOANS</li><li>SPLIT LOANS</li><li>LMI</li><li>FHOG</li></ul>
  </section>

  <aside class="abs consult">
    <div class="line1">CONSULT YOUR <b>tallyra</b></div>
    <div class="line2">MORTGAGE BROKER &amp; ACCOUNTANT</div>
    <div class="line3">WE'LL MAKE IT EASY.</div>
    <p>4/212 MARLOW RD LINFORD QLD 4190<br>07 3100 2481<br>ADMIN@TALLYRA.NET.AU</p>
  </aside>

  <p class="abs disclaimer">Tallyra Group Pty Ltd [Credit Representative Number 500127] is authorized under Australian Credit Licence Number 400862</p>
</main>
</body>
</html>
```